Brightstone Roofing Business Card

This is my current business card. But I’d like to make some changes. Somewhere on the card I’d like to list some of the services we offer. Maybe on the back? But I’d still like to keep the red. White and black modern look.

-residential & commercial roofing
-Roof Repairs & Maintenance
-Storm Damage & Insurance Claims specialist
-Christmas Lights and permanent Christmas lights
Fencing. Windows. Gutters. Siding. Sheetrock, painting.

```html
<!DOCTYPE html>
<html lang="en">
<head>
<meta charset="utf-8">
<title>Brightstone Roofing Business Card</title>
<link href="https://fonts.googleapis.com/css2?family=Michroma&family=Montserrat:wght@400;500&family=Oswald:wght@400&display=swap" rel="stylesheet">
<style>
  :root {
    --backdrop: #979797;
    --black: #000000;
    --red: #e51f24;
    --deep-red: #8f1a1d;
    --stripe-tone: #5c1a1c;
    --white: #ffffff;
    --muted: #c9c9c9;
    --rule: #4a4a4a;
  }
  * { margin: 0; padding: 0; box-sizing: border-box; }
  html, body { width: 1200px; height: 1000px; overflow: hidden; }
  body { background: var(--backdrop); position: relative; font-family: "Montserrat", sans-serif; }

  .card { position: absolute; width: 694px; height: 399px; border-radius: 24px; overflow: hidden; }

  /* Front */
  .card-front { left: 248px; top: 72px; background: var(--black); }
  .brand-block { position: absolute; left: 70px; top: 70px; width: 280px; text-align: center; }
  .brand-dot { width: 96px; height: 96px; border-radius: 50%; background: var(--red); margin: 0 auto 24px; }
  .brand-name { font-family: "Michroma", sans-serif; color: var(--white); font-size: 17px; line-height: 1.4; letter-spacing: 0.5px; }
  .divider-vertical { position: absolute; left: 349px; top: 48px; width: 1px; height: 212px; background: var(--rule); }
  .contact-block { position: absolute; left: 391px; top: 110px; }
  .person-name { font-family: "Michroma", sans-serif; font-size: 22px; color: var(--white); letter-spacing: 1px; line-height: 1; }
  .person-name .surname { color: var(--red); }
  .person-role { font-family: "Montserrat", sans-serif; font-size: 13px; color: var(--white); letter-spacing: 6px; margin-top: 8px; }
  .contact-list { list-style: none; margin-top: 16px; }
  .contact-list li { display: flex; align-items: center; gap: 10px; color: var(--white); font-size: 15px; line-height: 21px; }
  .contact-list svg { width: 14px; height: 14px; fill: var(--red); flex: none; }
  .divider-horizontal { position: absolute; left: 0; top: 282px; width: 660px; height: 1px; background: linear-gradient(90deg, var(--rule), #7a7a7a 50%, transparent); }
  .services { position: absolute; left: 20px; right: 20px; top: 304px; text-align: center; font-family: "Oswald", sans-serif; font-size: 16px; line-height: 25px; color: var(--muted); text-transform: uppercase; letter-spacing: 0.3px; }
  .services .sep { color: var(--red); padding: 0 3px; }

  /* Back */
  .card-back { left: 252px; top: 514px; background: var(--red); }
  .quad { position: absolute; }
  .quad-top-left { left: 0; top: 0; width: 446px; height: 251px; background: var(--deep-red); }
  .quad-top-right { left: 446px; top: 0; width: 248px; height: 251px; background: var(--red); }
  .quad-bottom-left { left: 0; top: 251px; width: 446px; height: 148px; background: var(--red); }
  .quad-bottom-right { left: 446px; top: 251px; width: 248px; height: 148px; background: var(--black); }
  .stripe-panel { position: absolute; left: 23px; top: 0; width: 190px; height: 399px; background: linear-gradient(180deg, var(--stripe-tone), #6e1b1e); }
  .back-dot { position: absolute; left: 376px; top: 60px; width: 140px; height: 140px; border-radius: 50%; background: var(--white); }
  .back-name { position: absolute; left: 220px; width: 452px; top: 284px; text-align: center; font-family: "Michroma", sans-serif; font-size: 30px; line-height: 1.35; color: var(--white); letter-spacing: 1px; }
</style>
</head>
<body>

<section class="card card-front">
  <div class="brand-block">
    <div class="brand-dot"></div>
    <p class="brand-name">BRIGHTSTONE<br>ROOFING CO.</p>
  </div>

  <div class="divider-vertical"></div>

  <div class="contact-block">
    <h1 class="person-name">DYLAN <span class="surname">MARSH</span></h1>
    <p class="person-role">OWNER</p>
    <ul class="contact-list">
      <li>
        <svg viewBox="0 0 24 24"><path d="M6.6 10.8a15.1 15.1 0 0 0 6.6 6.6l2.2-2.2c.3-.3.7-.4 1-.2 1.1.4 2.3.6 3.6.6.6 0 1 .4 1 1V20c0 .6-.4 1-1 1A17 17 0 0 1 3 4c0-.6.4-1 1-1h3.5c.6 0 1 .4 1 1 0 1.3.2 2.5.6 3.6.1.3 0 .7-.2 1z"/></svg>
        555-014-2298
      </li>
      <li>
        <svg viewBox="0 0 24 24"><path d="M2 5h20v14H2z M4 7v.5l8 5 8-5V7l-8 5z" fill-rule="evenodd"/></svg>
        dylan@brightstoneroofing.com
      </li>
      <li>
        <svg viewBox="0 0 24 24"><path d="M12 2a10 10 0 1 0 0 20 10 10 0 0 0 0-20zm0 2c.9 1.2 1.6 2.6 2 4h-4c.4-1.4 1.1-2.8 2-4zM4.3 14a8 8 0 0 1 0-4h3.4a16 16 0 0 0 0 4zm.8 2h3c.3 1.3.8 2.5 1.4 3.6A8 8 0 0 1 5.1 16zm3-8h-3a8 8 0 0 1 4.4-3.6C8.9 5.5 8.4 6.7 8.1 8zM12 20c-.9-1.2-1.6-2.6-2-4h4c-.4 1.4-1.1 2.8-2 4zm2.3-6H9.7a14 14 0 0 1 0-4h4.6a14 14 0 0 1 0 4zm.2 5.6c.6-1.1 1.1-2.3 1.4-3.6h3a8 8 0 0 1-4.4 3.6zM16.3 14a16 16 0 0 0 0-4h3.4a8 8 0 0 1 0 4z"/></svg>
        brightstoneroofing.com
      </li>
    </ul>
  </div>

  <div class="divider-horizontal"></div>

  <p class="services">
    Residential &amp; Commercial Roofing <span class="sep">•</span> Roof Repairs &amp; Maintenance Storm Damage &amp;<br>
    Insurance Claims Specialist <span class="sep">•</span> Christmas Lights and Permanent <span class="sep">•</span> Permanent Christmas<br>
    Lights <span class="sep">•</span> Fencing <span class="sep">•</span> Windows <span class="sep">•</span> Gutters <span class="sep">•</span> Siding • Sheetrock <span class="sep">•</span> Painting
  </p>
</section>

<section class="card card-back">
  <div class="quad quad-top-left"></div>
  <div class="quad quad-top-right"></div>
  <div class="quad quad-bottom-left"></div>
  <div class="quad quad-bottom-right"></div>
  <div class="stripe-panel" role="img" aria-label="Panel of diagonal dark stripes over red"></div>
  <div class="back-dot"></div>
  <p class="back-name">BRIGHTSTONE<br>ROOFING CO.</p>
</section>

</body>
</html>
```